Business Card Design

I need a design/ business card for a new company that caters for Event Hire (decorations and linen only) I am dabbling in rustic/ vintage designs for weddings and would like an elegant look to the cards. Something that will catch peoples eyes amongst the rest of the competitions cards and stand out to all fields, corporate/ weddings and general functions.

I am unsure of colours or pictures i would like so i am open to anything but possibly stick away from photos as i they are not more work of art on the card?

Target Market(s)

weddings and corporate events

Industry/Entity Type

Business

Contact Information for Business Card

Marlowe Weddings & Event Hire

Servicing the Gladstone Region for Weddings, Corporate & Private Functions

marloweweddings@postvane.com
Phone: 0427 813 542

Requirements
Must have
• The writing "Marlowe Weddings & Event Hire" please
Nice to have
• Something that really stands out as a must have at your event
Should not have
• Pictures that are not of my work

```html
<!DOCTYPE html>
<html lang="en">
<head>
<meta charset="utf-8">
<title>Marlowe Weddings &amp; Event Hire – Business Card</title>
<link rel="stylesheet" href="https://fonts.googleapis.com/css2?family=Pinyon+Script&family=Cormorant+Garamond:ital,wght@1,600&display=swap">
<style>
  :root {
    --blue-deep: #5478c2;
    --blue-mid: #7d9bd2;
    --blue-pale: #dde1ec;
    --ink: #28327a;
    --gold: #ffdc10;
    --amber-soft: rgba(236, 184, 96, 0.38);
    --white: #ffffff;
  }
  html, body {
    margin: 0;
    padding: 0;
    overflow: hidden;
    background: #ffffff;
  }
  .card {
    position: relative;
    width: 1200px;
    height: 741px;
    overflow: hidden;
    background:
      radial-gradient(ellipse 620px 460px at 1000px 140px, var(--blue-pale) 0%, rgba(221,225,236,0.6) 35%, rgba(125,155,210,0) 75%),
      linear-gradient(160deg, var(--blue-mid) 0%, var(--blue-deep) 70%);
  }
  .card__light-art {
    position: absolute;
    left: 0;
    top: 250px;
    width: 900px;
    height: 491px;
    background: radial-gradient(ellipse 520px 320px at 320px 300px, var(--amber-soft) 0%, rgba(236,184,96,0) 100%);
  }
  .card__title {
    position: absolute;
    left: 74px;
    top: 68px;
    margin: 0;
    font-family: "Pinyon Script", cursive;
    font-weight: 400;
    font-size: 104px;
    line-height: 124px;
    word-spacing: 8px;
    color: var(--white);
    text-shadow: 0 0 8px rgba(255,255,255,0.9), 0 0 18px rgba(255,255,255,0.6);
    white-space: nowrap;
  }
  .card__rule {
    position: absolute;
    left: 69px;
    top: 351px;
    width: 668px;
    height: 17px;
    background: var(--gold);
  }
  .card__tagline {
    position: absolute;
    left: 690px;
    top: 334px;
    width: 452px;
    margin: 0;
    font-family: "Cormorant Garamond", serif;
    font-style: italic;
    font-weight: 600;
    font-size: 46px;
    line-height: 38px;
    letter-spacing: 6px;
    text-align: center;
    white-space: nowrap;
    color: var(--ink);
  }
  .card__contact {
    position: absolute;
    right: 72px;
    top: 522px;
    margin: 0;
    font-family: "Cormorant Garamond", serif;
    font-style: italic;
    font-weight: 600;
    font-size: 45px;
    line-height: 43px;
    text-align: right;
    white-space: nowrap;
    color: var(--ink);
  }
  .card__contact span { display: block; }
</style>
</head>
<body>
  <main class="card">
    <div class="card__light-art" role="img" aria-label="Decorative area for swirling light ribbons in gold and amber"></div>
    <h1 class="card__title">Marlowe Weddings &amp;<br>Event Hire</h1>
    <div class="card__rule"></div>
    <p class="card__tagline">servicing the<br>Gladstone Region<br>for Weddings</p>
    <address class="card__contact">
      <span>corporate &amp; Private Functions</span>
      <span>marloweweddings@postvane.com</span>
      <span>Phone: 0427 813 542</span>
    </address>
  </main>
</body>
</html>
```